Personal Trainer Business Card

I need a business card using a logo I already have.
The logo is in uploaded files.
Card is to give to prospective clients that interested in health and beauty or already exercise. Would like logo on front or other abstract images and details on back.
Like modern design that also unique and eye catching rather than just generic fitness gym/fitness theme.

Target Market(s)

Main clients are trendy women aged 25-60.

Industry/Entity Type

Fitness

Contact Information for Business Card

Email: tom@tomharvecoaching.com

web: www.tomharvecoaching.com

mobile: 0493 257618

facebook: www.socialnook.com/tomharvecoaching

Location is: Wattle Heads

Font styles to use
Sans Serif

Colors
000000
1b1b1b
333333

Requirements
Must have
• Logo on front
• black background of sorts on front (fine if mixed with dark grey or abstract)
• White background on back.
Nice to have
• I would like the front side with the logo appearing on it with black background. Fine with alternative ideas and layout.
• Would like the front to be modern, professional and cool/interesting.
• Fine with abstract or modern design.
• Reverse of the card some white background with details on it
• (I like simple fonts).
• CAn use same font colour as in logo in places or what whatever
Should not have
• Avoiding use of cheap pics such as weights

```html
<!DOCTYPE html>
<html lang="en">
<head>
<meta charset="utf-8">
<title>Tom Harve Coaching – Business Card</title>
<link rel="stylesheet" href="https://fonts.googleapis.com/css2?family=Montserrat:wght@400;500;700&display=swap">
<style>
  :root {
    --backdrop: #2a2a2a;
    --card-black: #111111;
    --card-white: #ffffff;
    --silver: #c4c4c4;
    --ink: #1b1b1b;
    --ink-soft: #333333;
    --gold: #b8985a;
    --social-square: #3b5a9a;
  }
  * { box-sizing: border-box; margin: 0; padding: 0; }
  html, body { width: 1200px; height: 900px; overflow: hidden; }
  body {
    background: var(--backdrop);
    font-family: "Montserrat", Arial, sans-serif;
    position: relative;
  }
  .card {
    position: absolute;
    left: 280px;
    width: 640px;
    height: 366px;
    box-shadow: 0 10px 30px rgba(0,0,0,0.45);
  }
  .card-front { top: 60px; background: var(--card-black); }
  .card-back { top: 474px; background: var(--card-white); }

  .brand-name {
    font-weight: 700;
    letter-spacing: 0.06em;
    text-transform: uppercase;
    line-height: 1.1;
    white-space: nowrap;
  }
  .card-front .brand-name {
    position: absolute;
    left: 0; right: 0;
    top: 118px;
    text-align: center;
    font-size: 40px;
    color: var(--silver);
  }
  .social-line {
    position: absolute;
    left: 0; right: 0;
    top: 268px;
    display: flex;
    justify-content: center;
    align-items: center;
    gap: 8px;
    font-size: 15px;
    color: #e6e6e6;
  }
  .social-square {
    width: 11px; height: 11px;
    background: var(--social-square);
  }

  .card-back .brand-name {
    position: absolute;
    left: 34px;
    top: 80px;
    font-size: 26px;
    color: var(--ink-soft);
  }
  .divider {
    position: absolute;
    top: 176px;
    height: 1.5px;
    background: var(--gold);
  }
  .divider-left { left: 0; width: 318px; }
  .divider-right { left: 524px; right: 0; }
  .contact-block {
    position: absolute;
    left: 330px;
    top: 162px;
    color: var(--ink);
  }
  .person-name {
    font-size: 21px;
    font-weight: 700;
    line-height: 28px;
    color: var(--gold);
    letter-spacing: 0.04em;
    text-transform: uppercase;
    white-space: nowrap;
  }
  .person-role {
    font-size: 13px;
    font-weight: 700;
    letter-spacing: 0.04em;
    margin: 4px 0 2px 16px;
  }
  .contact-list {
    list-style: none;
    margin-left: 16px;
    font-size: 14px;
    color: var(--ink-soft);
  }
  .contact-list li { display: flex; align-items: center; gap: 8px; height: 20px; white-space: nowrap; }
  .icon-slot { width: 12px; height: 12px; flex: none; }
  .contact-list svg { width: 12px; height: 12px; flex: none; }
  .contact-list .web { font-weight: 700; color: var(--ink); }
</style>
</head>
<body>

<section class="card card-front">
  <div class="brand-name">Tom Harve Coaching</div>
  <div class="social-line">
    <span class="social-square"></span>
    <span>www.socialnook.com/tomharvecoaching</span>
  </div>
</section>

<section class="card card-back">
  <div class="brand-name">Tom Harve Coaching</div>
  <div class="divider divider-left"></div>
  <div class="divider divider-right"></div>
  <div class="contact-block">
    <div class="person-name">Mara Ellison</div>
    <div class="person-role">DIRECTOR</div>
    <ul class="contact-list">
      <li><span class="icon-slot"></span>Wattle Heads</li>
      <li>
        <svg viewBox="0 0 12 12" aria-hidden="true"><rect x="3" y="0.8" width="6" height="10.4" rx="1.2" fill="none" stroke="#b8985a" stroke-width="1.2"/><circle cx="6" cy="9.2" r="0.7" fill="#b8985a"/></svg>
        0493 257618
      </li>
      <li>
        <svg viewBox="0 0 12 12" aria-hidden="true"><rect x="0.8" y="2.5" width="10.4" height="7" fill="none" stroke="#b8985a" stroke-width="1.2"/><path d="M1 3 L6 7 L11 3" fill="none" stroke="#b8985a" stroke-width="1.2"/></svg>
        tom@tomharvecoaching.com
      </li>
      <li>
        <svg viewBox="0 0 12 12" aria-hidden="true"><circle cx="6" cy="6" r="5" fill="none" stroke="#b8985a" stroke-width="1.1"/><ellipse cx="6" cy="6" rx="2.2" ry="5" fill="none" stroke="#b8985a" stroke-width="1"/><path d="M1 6 H11" stroke="#b8985a" stroke-width="1"/></svg>
        <span class="web">www.tomharvecoaching.com</span>
      </li>
    </ul>
  </div>
</section>

</body>
</html>
```